New web design needed for our company

We need our website designing, it needs to be professional and look creative,
We are a plumbing and heating company called Kestrel Bay's (www.kestrelbays.co.uk)
I like this site design also some of the following maybe:
https://www.marnockheating.com/
http://www.tavelpower.co.uk

Please let me know when you want our logo files as it wont let me upload them

The design will require coding once the design is complete, i havent paid for this yet as i want to be sure the design is good before i commit.

The template needs to look professional and look like one of the leading companies.
The site will consist of all the features this site has https://www.marnockheating.com/

I like a modern design with the latest technology.

Must have a customer login page and a my account area

Target Market(s)

Everyone

Industry/Entity Type

Plumbing

Coding

Coded - Design and coding required

Number of Pages Required

5+ page

Font styles to use
Other font styles liked:
• whatever suites

Requirements
Must have
• The design will require coding once the design is complete, i havent paid for this yet as i want to be sure the design is good before i commit.
• The template needs to look professional and look like one of the leading companies.
• The site will consist of all the features this site has https://www.marnockheating.com/
• I like a modern design with the latest technology.
• Must have a customer login page and a my account area
Nice to have
• inspirational and different
Should not have
• plain boring designs like most plumbing websites, needs to be inspiring and attract people from first sight.

```html
<!DOCTYPE html>
<html lang="en">
<head>
<meta charset="utf-8">
<title>Kestrel Bay's – Your Local Experts</title>
<link href="https://fonts.googleapis.com/css2?family=Source+Sans+3:wght@400;600;700&display=swap" rel="stylesheet">
<style>
:root{
  --navy:#0b4a96;
  --navy-dark:#083a78;
  --orange:#f4563a;
  --sky:#cfe6fb;
  --ink:#222;
  --muted:#9aa3ad;
  --white:#fff;
}
*{margin:0;padding:0;box-sizing:border-box}
html,body{width:1104px;height:1200px;overflow:hidden;background:var(--white)}
body{position:relative;font-family:"Source Sans 3",Arial,sans-serif;color:var(--ink)}
.abs{position:absolute}

/* header */
.brand{left:110px;top:18px;font-size:38px;font-weight:700;color:var(--navy);letter-spacing:-1px;line-height:1;display:flex;align-items:center;gap:8px}
.brand-dot{width:12px;height:12px;border-radius:50%;background:var(--orange)}
.brand-tag{left:225px;top:57px;font-size:11px;color:var(--navy)}
.emergency{left:677px;top:0;width:316px;height:26px;background:var(--navy);clip-path:polygon(0 0,100% 0,96% 100%,4% 100%);color:var(--white);font-size:9px;display:flex;align-items:center;justify-content:center;gap:6px}
.emergency b{font-weight:700}
.nav{top:45px;left:366px;display:flex;gap:0;font-size:10.5px;text-transform:uppercase}
.nav a{color:var(--ink);text-decoration:none;margin-right:26px}
.nav a.active{color:var(--orange)}
.account{top:44px;left:792px;font-size:10.5px;display:flex;align-items:center;gap:5px}
.btn-quote{left:912px;top:41px;width:81px;height:24px;background:var(--orange);color:var(--white);font-size:10.5px;display:flex;align-items:center;justify-content:center}

/* hero */
.hero-bg{left:0;top:87px;width:1104px;height:355px;background:var(--sky)}
.hero-photo{left:0;top:87px;width:680px;height:355px;background:linear-gradient(100deg,#1e6fc2 0%,#6fb0ea 35%,#d7ebfb 75%,var(--sky) 100%)}
.form-tab{left:668px;top:442px;width:324px;height:18px;background:var(--navy-dark);clip-path:polygon(0 0,100% 0,96% 100%,4% 100%)}
.quote-form{left:679px;top:115px;width:302px;height:345px;background:var(--navy);padding:20px 23px}
.quote-form h2{color:var(--white);font-size:16px;font-weight:700;text-align:center;text-transform:uppercase;margin-bottom:13px}
.field{height:34px;background:var(--white);border-radius:2px;margin-bottom:11px;display:flex;align-items:center;justify-content:space-between;padding:0 10px;font-size:10px;font-weight:600;color:#b9bec4;letter-spacing:.3px}
.field.msg{height:83px;align-items:flex-start;padding-top:11px}
.submit{height:34px;background:var(--orange);color:var(--white);font-weight:700;font-size:12px;display:flex;align-items:center;justify-content:center;border-radius:2px;margin-top:4px}

/* services */
.section-title{left:110px;top:493px;font-size:23px;color:var(--navy)}
.section-title b{color:var(--orange);font-weight:700}
.service{top:553px;width:280px;height:184px}
.service .photo{width:100%;height:100%}
.service .label{position:absolute;left:-8px;top:138px;height:23px;padding:0 16px 0 22px;background:var(--navy);color:var(--white);font-size:11px;display:flex;align-items:center;text-transform:uppercase}
.service .label::after{content:"";position:absolute;left:0;top:23px;border-top:8px solid var(--navy-dark);border-left:8px solid transparent}

/* call to action */
.cta{left:0;top:809px;width:1104px;height:148px;background:linear-gradient(90deg,#5b84b6,#4f7cb1 60%,#6b90bd)}
.cta h3{left:165px;top:860px;font-size:21px;font-weight:400;color:var(--white)}
.cta-text{left:165px;top:886px;font-size:11.5px;font-weight:600;color:var(--white)}
.cta-btn{left:731px;top:868px;width:209px;height:30px;background:var(--orange);color:var(--white);font-size:11px;font-weight:600;display:flex;align-items:center;justify-content:center;text-transform:uppercase}

/* footer */
.col{top:1012px;font-size:9px;line-height:20.5px}
.col h4{font-size:10px;font-weight:700;color:var(--navy);margin-bottom:5px}
.col p{color:var(--ink)}
.col u{text-decoration:underline}
.news-text{line-height:13px;margin-bottom:10px}
.news-input{width:176px;height:27px;background:#eef0f2;display:flex;align-items:center;justify-content:space-between;padding:0 10px;font-size:9px;color:#555}
.rule{left:164px;top:1146px;width:778px;height:1px;background:#e1e4e7}
.copyright{left:164px;top:1164px;font-size:8.5px}
.social{top:1160px;width:22px;height:22px;border-radius:50%}
</style>
</head>
<body>

<!-- header -->
<div class="abs brand"><span class="brand-dot"></span>Kestrel Bay's</div>
<div class="abs brand-tag">Your Local Experts</div>
<div class="abs emergency">
  <svg width="10" height="10" viewBox="0 0 24 24"><path fill="#fff" d="M6.6 10.8a15 15 0 0 0 6.6 6.6l2.2-2.2c.3-.3.7-.4 1-.2 1.1.4 2.3.6 3.6.6.6 0 1 .4 1 1V20c0 .6-.4 1-1 1A17 17 0 0 1 3 4c0-.6.4-1 1-1h3.5c.6 0 1 .4 1 1 0 1.3.2 2.5.6 3.6.1.3 0 .7-.2 1z"/></svg>
  GOT A PLUMBING EMERGENCY? &nbsp;CALL US NOW: <b>01632 960 418</b>
</div>
<nav class="abs nav">
  <a class="active">Home</a><a>About Us</a><a>Services</a><a>Contact</a><a>Products</a><a>Testimonials</a>
</nav>
<div class="abs account">
  <svg width="12" height="12" viewBox="0 0 24 24"><circle cx="12" cy="7" r="5" fill="#0b4a96"/><path d="M2 23c0-6 4.5-9 10-9s10 3 10 9z" fill="#0b4a96"/></svg>
  SIGN IN &nbsp;| &nbsp;REGISTER
</div>
<div class="abs btn-quote">GET A QUOTE</div>

<!-- hero -->
<div class="abs hero-bg"></div>
<div class="abs hero-photo" role="img" aria-label="Photo of a shower head spraying water droplets"></div>
<div class="abs form-tab"></div>
<form class="abs quote-form">
  <h2>Need Plumbing Service?</h2>
  <div class="field">NAME <svg width="11" height="12" viewBox="0 0 24 24"><circle cx="12" cy="7" r="5" fill="#ccd0d4"/><path d="M2 23c0-6 4.5-9 10-9s10 3 10 9z" fill="#ccd0d4"/></svg></div>
  <div class="field">EMAIL <svg width="12" height="9" viewBox="0 0 24 16"><rect width="24" height="16" fill="#ccd0d4"/><path d="M0 0l12 9 12-9" stroke="#fff" stroke-width="2" fill="none"/></svg></div>
  <div class="field">PHONE <svg width="8" height="12" viewBox="0 0 14 22"><rect width="14" height="22" rx="2" fill="#ccd0d4"/></svg></div>
  <div class="field msg">YOUR MESSAGE</div>
  <div class="submit">REQUEST QUOTE</div>
</form>

<!-- services -->
<h2 class="abs section-title">OUR <b>SERVICES</b></h2>
<div class="abs service" style="left:110px">
  <div class="photo" role="img" aria-label="Photo of a white radiator beside stairs" style="background:linear-gradient(90deg,#c9cccf,#eceeef 50%,#d9dcde)"></div>
  <div class="label">Central Heating</div>
</div>
<div class="abs service" style="left:412px">
  <div class="photo" role="img" aria-label="Photo of a hand fitting a black drain pipe under a sink" style="background:linear-gradient(135deg,#d8dde2,#3a4150 55%,#e7e9ec)"></div>
  <div class="label">Plumbing</div>
</div>
<div class="abs service" style="left:714px">
  <div class="photo" role="img" aria-label="Photo of an engineer adjusting a gas boiler" style="background:linear-gradient(90deg,#2f4f86,#7f97bd 45%,#e9ecef)"></div>
  <div class="label">Gas Fitting</div>
</div>

<!-- call to action -->
<div class="abs cta" role="img" aria-label="Photo of a hand holding a wrench on a chrome pipe, tinted blue"></div>
<h3 class="abs cta" style="background:none;width:auto;height:auto;left:165px;top:860px;font-size:21px;font-weight:400;color:#fff">Do You Need Any Help?</h3>
<p class="abs cta-text">Aenean eu leo quam. Pellentesque ornare sem lacinia quam venenatis vestibulum.</p>
<div class="abs cta-btn">Contact Now For Our Services</div>

<!-- footer -->
<div class="abs col" style="left:164px">
  <h4>&nbsp;Contact Us</h4>
  <p>@: <u>contact@kestrelbays.co.uk</u></p>
  <p>p: +44 1632 960 418</p>
  <p style="line-height:14px;margin-top:3px">a: The Name of The Street 323<br>&nbsp;&nbsp;&nbsp;Scotland, United Kingdom 49009</p>
</div>
<div class="abs col" style="left:363px">
  <h4>Company</h4>
  <p>Home</p><p>About Us</p><p>Services</p><p>Contact Us</p>
</div>
<div class="abs col" style="left:562px">
  <h4>Others</h4>
  <p>Help &amp; Support</p><p>Privacy Policy</p><p>Terms</p><p>Sitemap</p>
</div>
<div class="abs col" style="left:764px">
  <h4>Newsletter</h4>
  <p class="news-text">Subscribe to our newsletter and get all<br>the cool news</p>
  <div class="news-input">Enter Email
    <svg width="13" height="13" viewBox="0 0 24 24"><path d="M22 2L2 10l8 3 3 8z M22 2L10 13" fill="none" stroke="#0b4a96" stroke-width="2" stroke-linejoin="round"/></svg>
  </div>
</div>
<div class="abs rule"></div>
<p class="abs copyright">All rights reserved 2016.</p>
<div class="abs social" style="left:859px;background:#3a9ee6"></div>
<div class="abs social" style="left:889px;background:#1f4f9c"></div>
<div class="abs social" style="left:918px;background:#2f6fb4"></div>

</body>
</html>
```